Square Business Cards for Our Restaurant / Event Venue

We need square business cards designed for the management team of our event venue and restaurant. On one side of the card should be the the Lantern Hall 7 logo and URL www.lanternhall7.example. On the other side should be the Ember Logo and URL www.emberonfive.example. All employee details should be on the side with Ember logo. There will be a total of 5 cards to be created with the design.

Corinne Baldrath
corinne@lanternhall7.example

main 202.555.4817
direct 202.555.0392

3418 Westbury Lane NW
Washington, DC 20019

```html
<!DOCTYPE html>
<html lang="en">
<head>
<meta charset="utf-8">
<title>Ember / Lantern Hall 7 business cards</title>
<link rel="stylesheet" href="https://fonts.googleapis.com/css2?family=Roboto:wght@400;500;700&display=swap">
<style>
  :root {
    --backdrop: #e9e7e4;
    --card-white: #f6f6f6;
    --brand-red: #b71c1f;
    --ink-black: #0e0e0e;
    --text-white: #ffffff;
    --text-grey: #4a4a4a;
  }
  * { margin: 0; padding: 0; box-sizing: border-box; }
  html, body {
    width: 1200px; height: 960px; overflow: hidden;
    background: var(--backdrop);
    font-family: "Roboto", Arial, sans-serif;
  }
  .canvas { position: relative; width: 1200px; height: 960px; }
  .card {
    position: absolute; width: 600px; height: 341px;
    background: var(--card-white); overflow: hidden;
  }
  .card--front { left: 302px; top: 130px; }
  .card--back { left: 299px; top: 489px; }
  .front-wave { position: absolute; inset: 0; width: 600px; height: 341px; }
  .brand-name {
    position: absolute; left: 70px; top: 66px;
    font-size: 72px; font-weight: 500; color: var(--ink-black);
    line-height: 1;
  }
  .contact {
    position: absolute; right: 30px; top: 138px;
    text-align: right; color: var(--text-white);
  }
  .contact__name { font-size: 20px; font-weight: 500; line-height: 22px; }
  .contact__role { font-size: 14.5px; font-weight: 500; line-height: 18px; }
  .contact__address { font-size: 14.5px; line-height: 20px; margin-top: 10px; }
  .contact__lines { list-style: none; margin-top: 8px; font-size: 14.5px; line-height: 19.5px; }
  .contact__lines li { display: flex; justify-content: flex-end; align-items: center; gap: 9px; }
  .contact__lines svg { width: 13px; height: 13px; flex: none; }
  .venue-mark {
    position: absolute; left: 206px; top: 61px;
    width: 190px; height: 190px; border-radius: 50%;
    background: var(--brand-red);
    display: flex; align-items: center; justify-content: center;
  }
  .venue-name {
    color: var(--text-white); font-size: 25px; font-weight: 400;
    text-align: center; line-height: 1.2;
  }
  .venue-url {
    position: absolute; left: 0; right: 0; top: 290px;
    text-align: center; font-size: 14px; letter-spacing: 3px; color: var(--text-grey);
  }
  .venue-url span { color: var(--brand-red); }
</style>
</head>
<body>
<main class="canvas">
  <section class="card card--front">
    <svg class="front-wave" viewBox="0 0 600 341" aria-hidden="true">
      <path d="M0,212 C90,266 200,282 284,222 C324,172 374,92 444,54 C496,30 570,34 600,44 L600,341 L0,341 Z" fill="var(--ink-black)"/>
      <path d="M0,228 C90,281 200,296 288,236 C328,186 378,106 448,66 C498,41 570,44 600,54 L600,341 L0,341 Z" fill="#ffffff"/>
      <path d="M0,232 C90,285 200,300 290,240 C330,190 380,110 450,70 C500,45 570,48 600,58 L600,341 L0,341 Z" fill="var(--brand-red)"/>
    </svg>
    <div class="brand-name">Ember</div>
    <div class="contact">
      <p class="contact__name">CORINNE BALDRATH</p>
      <p class="contact__role">CEO/FOUNDER</p>
      <p class="contact__address">3418 Westbury Lane NW<br>Washington, DC 20019</p>
      <ul class="contact__lines">
        <li>202.555.4817
          <svg viewBox="0 0 16 16"><path fill="#fff" d="M3.5 1l2.5 3-1.5 2c1 2 3 4 5 5l2-1.5 3 2.5-2 2.5C7 15 1 9 1 3.5z"/></svg></li>
        <li>202.555.0392
          <svg viewBox="0 0 16 16"><path fill="#fff" d="M3.5 1l2.5 3-1.5 2c1 2 3 4 5 5l2-1.5 3 2.5-2 2.5C7 15 1 9 1 3.5z"/></svg></li>
        <li>corinne@lanternhall7.example
          <svg viewBox="0 0 16 16"><rect x="1" y="3" width="14" height="10" fill="#fff"/><path d="M1 3l7 6 7-6" fill="none" stroke="var(--brand-red)" stroke-width="1.4"/></svg></li>
        <li>www.emberonfive.example
          <svg viewBox="0 0 16 16"><circle cx="8" cy="8" r="7" fill="#fff"/><path d="M1 8h14M8 1c-3 3-3 11 0 14M8 1c3 3 3 11 0 14" fill="none" stroke="var(--brand-red)" stroke-width="1.2"/></svg></li>
      </ul>
    </div>
  </section>

  <section class="card card--back">
    <div class="venue-mark"><p class="venue-name">Lantern Hall 7</p></div>
    <p class="venue-url">www.<span>lanternhall7</span>.example</p>
  </section>
</main>
</body>
</html>
```